marlow keyhaven.com

we are a new company that offer people that have lost there bit coin transaction a recovery and retrieval service
We are looking for a website that will allow you to fill in your details

name
email
bitcoins or other crypto lost and date of transaction

and then an auto reply to them from a given email to verify there email

I am looking for an easy for the client to leave there interest and has a security look around it and looks familiar to the user.

https://tandrelpath.info/?gclid=Xq7LmPzTgRWbNcEvHsKyDa3UjFoeIq92hQ4nBvtzYc5rWpLm8-k2-fAdGxuoTjQe_NsVbHwMzYqEcPlKrUsDa_qwXz

https://osmerlinkgroup.com

https://www.frendaxo.com/faq-items/restoring-your-account-access/

Target Market(s)

early investors into crypto

Industry/Entity Type

It Company

Logo Text

MARLOW KEYHAVEN/FINDERS

Coding

Coded - Design and coding required

Number of Pages Required

3 page

Requirements
Must have
• be able to :
• complete
• Name,
• Email
• transaction date of exchange and how much they invested

```html
<!DOCTYPE html>
<html lang="en">
<head>
<meta charset="utf-8">
<title>Marlow Keyhaven – Recovery and Retrieval</title>
<link href="https://fonts.googleapis.com/css2?family=Roboto:wght@400;500;700;900&family=Open+Sans:wght@400;600;700&display=swap" rel="stylesheet">
<style>
:root{
  --brand-blue:#1d3f8f;
  --ink:#111111;
  --text:#666666;
  --muted:#888888;
  --line:#d6d6d6;
  --soft-bg:#eef0f4;
  --footer:#262626;
  --footer-bottom:#1c1c1c;
  --white:#ffffff;
}
*{box-sizing:border-box;margin:0;padding:0}
html,body{width:1200px;height:2786px;overflow:hidden}
body{position:relative;background:var(--white);font-family:"Open Sans",Arial,sans-serif;color:var(--text)}
.abs{position:absolute}

/* top bar */
.topbar{left:0;top:0;width:1200px;height:34px;background:var(--brand-blue);color:var(--white);font-size:13px}
.topbar .login{left:100px;top:8px}
.topbar .cta{right:100px;top:6px;display:flex;align-items:center;gap:8px;font-size:13px}
.topbar .cta strong{font-family:"Roboto",sans-serif;font-size:16px;font-weight:700}
.topbar .social{display:flex;gap:8px;margin-left:6px}
.topbar .social span{width:9px;height:9px;border-radius:50%;background:var(--white);display:block}

/* hero */
.hero{left:0;top:34px;width:1200px;height:553px;overflow:hidden;
  background:linear-gradient(180deg,#8e97a5 0%,#a4a9b0 45%,#b4a68a 80%,#c4ad80 100%)}
.logo{display:flex;align-items:center;gap:10px}
.logo .mark{width:34px;height:34px;background:var(--white);display:block}
.logo .name{font-family:"Roboto",sans-serif;font-weight:700;font-size:20px;color:var(--white);line-height:1.05;width:120px}
.hero .logo{left:98px;top:22px}
.nav{left:474px;top:30px;display:flex;align-items:center;font-family:"Roboto",sans-serif;font-size:15px;color:var(--white)}
.nav a{padding:6px 10px;margin-right:16px;color:var(--white);text-decoration:none}
.nav a.active{border:1px solid var(--white)}
.hero h1{left:98px;top:190px;font-family:"Roboto",sans-serif;font-weight:900;font-size:45px;color:var(--white);letter-spacing:.5px}
.hero .sub{left:98px;top:248px;font-family:"Roboto",sans-serif;font-weight:700;font-size:20px;line-height:28px;color:var(--white)}
.hero .btn{left:98px;top:324px;width:175px;height:48px;border:2px solid var(--white);border-radius:4px;color:var(--white);
  font-weight:700;font-size:15px;display:flex;align-items:center;justify-content:center}
.hero .dots{left:584px;top:491px;display:flex;gap:4px}
.hero .dots span{width:8px;height:8px;border-radius:50%;border:1px solid var(--white)}
.hero .dots span.on{background:var(--white)}

/* what we do */
.intro-bg{left:0;top:587px;width:1200px;height:373px;background:var(--soft-bg)}
.section-title{font-family:"Roboto",sans-serif;font-weight:500;font-size:28px;color:var(--ink);text-align:center;width:1200px;left:0}
.intro-title{top:662px}
.intro-text{left:128px;top:720px;width:944px;text-align:center;font-size:13px;line-height:27px;color:var(--text)}
.video{left:236px;top:830px;width:728px;height:325px;border:1px solid #ddd;
  background:linear-gradient(120deg,#f1c7b3 0%,#e6b09a 50%,#e9d6cd 100%)}

/* contact form */
.form-box{left:98px;top:1260px;width:463px;height:382px;border:1px solid var(--line)}
.form-title{left:180px;top:1242px;padding:0 16px;background:var(--white);font-family:"Roboto",sans-serif;font-weight:500;font-size:26px;color:var(--ink)}
.field{left:145px;width:370px;height:37px;border:1px solid #cfcfcf;font-size:13px;color:var(--muted);padding:9px 13px}
.field.area{height:73px}
.send{left:299px;top:1566px;width:60px;height:31px;background:var(--brand-blue);color:var(--white);border-radius:4px;font-weight:700;font-size:12px;display:flex;align-items:center;justify-content:center}

/* how it works */
.how-title{left:600px;top:1240px;font-family:"Roboto",sans-serif;font-weight:500;font-size:28px;color:var(--ink)}
.how-lead{left:600px;top:1287px;width:495px;font-size:12.5px;line-height:28px}
.step{left:600px;width:500px}
.step svg{position:absolute;left:2px;top:0}
.step h3{position:absolute;left:74px;top:0;font-family:"Roboto",sans-serif;font-weight:500;font-size:15px;color:var(--ink)}
.step p{position:absolute;left:74px;top:28px;width:350px;font-size:12.5px;line-height:26px}

/* blog */
.blog-title{top:1720px}
.card{width:312px}
.card .photo{width:312px;height:247px;top:0;left:0;position:absolute}
.card p{position:absolute;top:272px;left:0;width:312px;font-size:12.5px;line-height:26.5px;color:#555;text-align:justify}
.card .meta{position:absolute;top:448px;left:0;width:312px;display:flex;align-items:center;font-size:10px;color:#555;gap:5px}
.card .meta b{font-weight:700;font-size:13px;color:var(--brand-blue);margin-right:16px}
.card .meta i{display:inline-block;width:9px;height:9px;background:var(--brand-blue)}

/* footer */
.footer{left:0;top:2355px;width:1200px;height:351px;background:var(--footer);color:var(--white)}
.footer .logo{left:98px;top:78px}
.footer .about{left:100px;top:112px;width:290px;font-size:12.5px;line-height:27px}
.footer h4{position:absolute;font-family:"Roboto",sans-serif;font-weight:500;font-size:24px}
.footer ul{position:absolute;list-style:none;font-size:12.5px;line-height:26.5px}
.footer .contact-list{left:898px;top:118px;font-size:12.5px;line-height:26.5px}
.footer .contact-list div{position:relative;padding-left:30px}
.footer .contact-list svg{position:absolute;left:0;top:8px}
.bottom{left:0;top:2706px;width:1200px;height:80px;background:var(--footer-bottom);color:var(--white);font-size:12px;text-align:center;padding-top:32px}
</style>
</head>
<body>

<div class="abs topbar">
  <div class="abs login">Log in / Sign up</div>
  <div class="abs cta"><strong>Get Your Bitcoin Back?</strong> <u>Mail</u> or <u>Call now</u> <span>|</span>
    <span class="social"><span></span><span></span><span></span><span></span></span></div>
</div>

<header class="abs hero" role="img" aria-label="Photo of a stack of gold coins with one large coin in focus">
  <div class="abs logo"><span class="mark"></span><span class="name">Marlow Keyhaven</span></div>
  <nav class="abs nav">
    <a class="active">Home</a><a>About Us</a><a>Services</a><a>Wallet</a><a>Pages</a><a>Blog</a><a>Contact us</a>
    <svg width="16" height="16" viewBox="0 0 16 16"><circle cx="6.5" cy="6.5" r="5" fill="none" stroke="#fff" stroke-width="2"/><line x1="10.5" y1="10.5" x2="15" y2="15" stroke="#fff" stroke-width="2.4"/></svg>
  </nav>
  <h1 class="abs">MARLOW KEYHAVEN</h1>
  <div class="abs sub">people that have lost there bit coin transaction<br>a recovery and retrieval service</div>
  <div class="abs btn">GET MORE INFO</div>
  <div class="abs dots"><span class="on"></span><span></span><span></span></div>
</header>

<div class="abs intro-bg"></div>
<h2 class="abs section-title intro-title">What we do</h2>
<p class="abs intro-text">Lorem Ipsum is simply dummy text of the printing and typesetting industry. Lorem Ipsum has been the industry's standard dummy text ever since the 1500s, when an unknown printer took a galley of type and scrambled it to make a type specimen book. It has survived not only five centuries, but also the leap into electronic typesetting, remaining essentially unchanged.</p>
<div class="abs video" role="img" aria-label="Video still of hands holding a smartphone showing the company name on the screen"></div>

<div class="abs form-box"></div>
<h2 class="abs form-title">Quick Contact Form</h2>
<div class="abs field" style="top:1311px">Your Name</div>
<div class="abs field" style="top:1360px">Your Email</div>
<div class="abs field" style="top:1408px">Date of transaction</div>
<div class="abs field area" style="top:1456px">Which cryptocurrency are you trying to recover?</div>
<div class="abs send">SEND</div>

<h2 class="abs how-title">How It Works</h2>
<p class="abs how-lead">It is a long established fact that a reader will be distracted by the readable tent of a page when looking at its layout.</p>

<div class="abs step" style="top:1362px">
  <svg width="44" height="40" viewBox="0 0 44 40"><rect x="2" y="6" width="36" height="30" rx="3" fill="none" stroke="#1d3f8f" stroke-width="2"/><rect x="26" y="15" width="16" height="12" rx="2" fill="none" stroke="#1d3f8f" stroke-width="2"/><circle cx="31" cy="21" r="2" fill="#1d3f8f"/></svg>
  <h3>Lost your Bitcoin wallet?</h3>
  <p>Excepteur sint occaecat cupidatat non proident, sunt in culpa qui officia deserunt mollit anim id est laborum</p>
</div>
<div class="abs step" style="top:1470px">
  <svg width="44" height="44" viewBox="0 0 44 44"><path d="M4 20h8v20H4zM12 22l8-14c2-4 7-3 6 2l-2 8h12c3 0 4 3 3 5l-4 14c-1 2-2 3-4 3H12" fill="none" stroke="#1d3f8f" stroke-width="2" stroke-linejoin="round"/></svg>
  <h3>WE can help</h3>
  <p>Excepteur sint occaecat cupidatat non proident, sunt in culpa qui officia deserunt mollit anim id est laborum</p>
</div>
<div class="abs step" style="top:1570px">
  <svg width="44" height="44" viewBox="0 0 44 44"><circle cx="20" cy="22" r="18" fill="none" stroke="#1d3f8f" stroke-width="2"/><circle cx="20" cy="22" r="8" fill="none" stroke="#1d3f8f" stroke-width="2"/><line x1="7" y1="9" x2="33" y2="35" stroke="#1d3f8f" stroke-width="2"/></svg>
  <h3>No charge unless we succeed</h3>
  <p>Excepteur sint occaecat cupidatat non proident, sunt in culpa qui officia deserunt mollit anim id est laborum</p>
</div>

<h2 class="abs section-title blog-title">From The Blog</h2>

<article class="abs card" style="left:98px;top:1804px">
  <div class="photo" role="img" aria-label="Photo of a businessman in a suit talking on a phone in a car" style="background:linear-gradient(180deg,#dde4ec 0%,#a9b7c7 100%)"></div>
  <p>Sed ut perspiciatis unde omnis iste natus error sit voluptatem accusantium doloremque laudantium, totam rem aperiam, eaque ipsa quae ab illotore tatis et quasi architecto beatae vitae dicta sunt cabo. Nemo enim ipsam voluptatem quia luptas sit natur aut odit aut fugit,</p>
  <div class="meta"><b>READ MORE</b> Posted on <i></i> August 15, 2017 by <i></i> admin</div>
</article>
<article class="abs card" style="left:444px;top:1804px">
  <div class="photo" role="img" aria-label="Photo of hands at a keyboard overlaid with coins" style="background:linear-gradient(180deg,#c2a69b 0%,#8f8188 100%)"></div>
  <p>Sed ut perspiciatis unde omnis iste natus error sit voluptatem accusantium doloremque laudantium, totam rem aperiam, eaque ipsa quae ab illotore tatis et quasi architecto beatae vitae dicta sunt cabo. Nemo enim ipsam voluptatem quia luptas sit natur aut odit aut fugit,</p>
  <div class="meta"><b>READ MORE</b> Posted on <i></i> August 15, 2017 by <i></i> admin</div>
</article>
<article class="abs card" style="left:789px;top:1804px">
  <div class="photo" role="img" aria-label="Photo of a coin and paper notes resting on a laptop keyboard" style="background:linear-gradient(180deg,#4b4e53 0%,#1c1d20 100%)"></div>
  <p>Sed ut perspiciatis unde omnis iste natus error sit voluptatem accusantium doloremque laudantium, totam rem aperiam, eaque ipsa quae ab illotore tatis et quasi architecto beatae vitae dicta sunt cabo. Nemo enim ipsam voluptatem quia luptas sit natur aut odit aut fugit,</p>
  <div class="meta"><b>READ MORE</b> Posted on <i></i> August 15, 2017 by <i></i> admin</div>
</article>

<footer class="abs footer">
  <div class="abs logo"><span class="mark"></span><span class="name">Marlow Keyhaven</span></div>
  <p class="abs about">But I must explain to you how all this mistaken idea of denouncing pleasure and praising pain was born and I will give you a complete</p>
  <h4 style="left:472px;top:76px">Company</h4>
  <ul style="left:472px;top:124px"><li>About us</li><li>Team</li><li>Career</li><li>Blog</li></ul>
  <h4 style="left:682px;top:80px">Links</h4>
  <ul style="left:684px;top:122px"><li>Home</li><li>About Us</li><li>Services</li><li>Wallet</li><li>Pages</li><li>Blog</li><li>Contact us</li></ul>
  <h4 style="left:898px;top:78px">Contact us</h4>
  <div class="abs contact-list">
    <div><svg width="10" height="13" viewBox="0 0 10 13"><path d="M5 0a5 5 0 0 1 5 5c0 3-5 8-5 8S0 8 0 5a5 5 0 0 1 5-5z" fill="#fff"/><circle cx="5" cy="5" r="1.8" fill="#262626"/></svg>Lorem ipsum dolor sit amet,<br>consectetur adipiscing elit</div>
    <div><svg width="13" height="10" viewBox="0 0 13 10"><rect width="13" height="10" fill="#fff"/><path d="M0 0l6.5 5L13 0" fill="none" stroke="#262626" stroke-width="1.2"/></svg>info@marlowkeyhaven.com</div>
    <div><svg width="12" height="12" viewBox="0 0 12 12"><path d="M2 0l3 3-1.5 2a7 7 0 0 0 3.5 3.5L9 7l3 3-2 2C5 12 0 7 0 2z" fill="#fff"/></svg>(800) 555-0148</div>
  </div>
</footer>
<div class="abs bottom">©Copyrights2018 Marlow Keyhaven.All Rights Reserved</div>

</body>
</html>
```